The Brightwater Compass Business Card

We need an attractive business card with the logo that we bought from ArtVantly last year.
Our mission is to contribute to change the way today's leaders manage business companies bringing value to the workplace and helping them to build a new model of creating wealth.
Our logo is clear about our values : we seek Positive Change through People and are convinced that the pursuit of individual well-being and the chase of economic results can converge with the right management.
Management Consulting
Corinne Fabrelle
+34 612 98 70 31
corinne.fabrelle@thebrightwatercompass-mail.net
www.thebrightwatercompass-mail.net

```html
<!DOCTYPE html>
<html lang="en">
<head>
<meta charset="utf-8">
<title>The Brightwater Compass — Business Card</title>
<link href="https://fonts.googleapis.com/css2?family=Cinzel:wght@400;600&family=Roboto:wght@400&display=swap" rel="stylesheet">
<style>
  :root {
    --backdrop: #4a413b;
    --card-black: #1d1e20;
    --card-edge: #141516;
    --ink-white: #f1f1f1;
    --ink-soft: #d9d9d9;
    --teal: #2a8c8c;
    --gloss: #3a3b3e;
  }
  * { margin: 0; padding: 0; box-sizing: border-box; }
  html, body { width: 1200px; height: 716px; overflow: hidden; }
  body {
    background: var(--backdrop);
    position: relative;
    font-family: "Roboto", Arial, sans-serif;
  }
  .card {
    position: absolute;
    background: var(--card-black);
    border-radius: 4px;
    box-shadow: 0 6px 0 var(--card-edge), 0 14px 30px rgba(0,0,0,.45);
    overflow: hidden;
  }
  .card-back { left: 70px; top: 190px; width: 500px; height: 290px; }
  .card-front { left: 620px; top: 190px; width: 510px; height: 290px; }

  .back-mark {
    position: absolute; inset: 0;
    display: flex; align-items: center; justify-content: center; gap: 14px;
  }
  .back-mark .dot { width: 18px; height: 18px; border-radius: 50%; background: var(--gloss); }
  .back-mark .name {
    font-family: "Cinzel", Georgia, serif; font-weight: 600;
    font-size: 22px; color: var(--gloss); letter-spacing: 1px;
  }

  .brand {
    position: absolute; left: 34px; top: 30px;
    font-family: "Cinzel", Georgia, serif; font-weight: 600;
    font-size: 21px; color: var(--ink-white); letter-spacing: .5px;
  }
  .brand-rule {
    position: absolute; left: 34px; top: 62px; width: 300px; height: 1px;
    background: var(--ink-white); opacity: .8;
  }
  .person {
    position: absolute; left: 34px; top: 120px;
    font-family: "Cinzel", Georgia, serif; font-weight: 400;
    font-size: 20px; color: var(--teal); letter-spacing: 1px;
  }
  .contacts { position: absolute; left: 34px; top: 160px; list-style: none; }
  .contacts li {
    display: flex; align-items: center; gap: 10px;
    font-size: 12.5px; color: var(--ink-soft); line-height: 22px;
  }
  .contacts svg { width: 12px; height: 12px; fill: var(--teal); flex: none; }
  .emblem-area {
    position: absolute; right: -50px; bottom: -60px;
    width: 210px; height: 210px; border-radius: 50%;
    background: var(--teal);
  }
</style>
</head>
<body>
  <section class="card card-back" aria-label="Card back">
    <div class="back-mark">
      <span class="dot"></span>
      <span class="name">The Brightwater Compass</span>
    </div>
  </section>

  <section class="card card-front" aria-label="Card front">
    <div class="brand">The Brightwater Compass</div>
    <div class="brand-rule"></div>
    <div class="person">Corinne Fabrelle</div>
    <ul class="contacts">
      <li>
        <svg viewBox="0 0 24 24"><path d="M6.6 10.8a15 15 0 0 0 6.6 6.6l2.2-2.2a1 1 0 0 1 1-.25 11.4 11.4 0 0 0 3.6.6 1 1 0 0 1 1 1V20a1 1 0 0 1-1 1A17 17 0 0 1 3 4a1 1 0 0 1 1-1h3.5a1 1 0 0 1 1 1c0 1.25.2 2.45.6 3.6a1 1 0 0 1-.25 1z"/></svg>
        +34 612 98 70 31
      </li>
      <li>
        <svg viewBox="0 0 24 24"><path d="M12 2a10 10 0 1 0 0 20 10 10 0 0 0 0-20zm6.9 6h-2.9a15.6 15.6 0 0 0-1.4-3.6A8 8 0 0 1 18.9 8zM12 4c.8 1.2 1.5 2.5 1.9 4h-3.8c.4-1.5 1.1-2.8 1.9-4zM4.3 14a8 8 0 0 1 0-4h3.4a16 16 0 0 0 0 4zm.8 2h2.9c.3 1.3.8 2.5 1.4 3.6A8 8 0 0 1 5.1 16zM8 8H5.1a8 8 0 0 1 4.3-3.6C8.8 5.5 8.3 6.7 8 8zm4 12c-.8-1.2-1.5-2.5-1.9-4h3.8c-.4 1.5-1.1 2.8-1.9 4zm2.3-6H9.7a14.7 14.7 0 0 1 0-4h4.6a14.7 14.7 0 0 1 0 4zm.3 5.6c.6-1.1 1.1-2.3 1.4-3.6h2.9a8 8 0 0 1-4.3 3.6zM16.3 14a16 16 0 0 0 0-4h3.4a8 8 0 0 1 0 4z"/></svg>
        www.thebrightwatercompass-mail.net
      </li>
      <li>
        <svg viewBox="0 0 24 24"><path d="M2 5h20v14H2zm2 2v.5l8 5 8-5V7zm0 2.8V17h16V9.8l-8 5z"/></svg>
        corinne.fabrelle@thebrightwatercompass-mail.net
      </li>
    </ul>
    <div class="emblem-area" role="img" aria-label="Brand emblem area in teal"></div>
  </section>
</body>
</html>
```